business card with 2 locations on 1 card

I need a modern looking business card that I would use at 2 different locations. Possibly 1 location on 1 side and other location on other side. One should be able to distinguish the 2 locations immediately before having to read the address or description on card. You can take a look at my website to see what I'm drawn to. The logo is brand new that I just purchased on Craft Hive. I want to emphasize family.
Updates

Let's not use the yellow and blue colors. Added Thursday, August 31, 2017

Target Market(s)

women and children

Industry/Entity Type

Health And Wellness

Contact Information for Business Card

Business name: Willow Brook Chiropractic & Acupuncture
My name: Lorin Daske
Job title: DC, MAOM, LAc (CA), CNS

Location 1
Address: 4817 Marlowe Blvd, Suite B-100, Frisco, TX 75034
Phone: (469) 555-0182
Fax: (972) 555-0137

Location 2
Address: 1936 Belvane Road, Suite 100, Plano, TX 75075
Phone: (469) 555-0169
Fax: (972) 555-0137

Email: drlorindaske@mailnest.example
Website: www.drlorindaske.example

Font styles to use
Serif
Sans Serif

Colors

Designer to choose colors to be used in the design.

Requirements
Must have
• distinction between 2 locations.
Nice to have
• Colors preference below is there. But I like to see what you come up with too!

```html
<!DOCTYPE html>
<html lang="en">
<head>
<meta charset="utf-8">
<title>Willow Brook Chiropractic &amp; Acupuncture – Business Cards</title>
<link href="https://fonts.googleapis.com/css2?family=Cinzel:wght@400;600&family=Open+Sans:wght@400;600&display=swap" rel="stylesheet">
<style>
  :root {
    --backdrop: #4a4441;
    --card: #121212;
    --card-edge: #1d1d1d;
    --green: #8cd35a;
    --green-dark: #2f8a3a;
    --teal: #2f6f6c;
    --silver: #c9c9c9;
    --text: #e8e8e8;
  }
  * { margin: 0; padding: 0; box-sizing: border-box; }
  html, body { width: 1200px; height: 900px; overflow: hidden; }
  body {
    background: var(--backdrop);
    font-family: "Open Sans", Arial, sans-serif;
    color: var(--text);
    display: flex;
    align-items: center;
    justify-content: center;
    gap: 50px;
  }
  .card {
    width: 525px;
    height: 300px;
    background: var(--card);
    border: 1px solid var(--card-edge);
    box-shadow: 0 14px 30px rgba(0,0,0,.45);
    position: relative;
  }

  /* Location 1 – Frisco */
  .card--frisco { display: flex; align-items: center; }
  .brand-name {
    width: 210px;
    display: flex;
    align-items: center;
    justify-content: center;
    gap: 10px;
  }
  .brand-dot {
    width: 14px; height: 14px;
    border-radius: 50%;
    background: var(--teal);
    flex: none;
  }
  .brand-text {
    font-family: "Cinzel", Georgia, serif;
    font-weight: 600;
    font-size: 20px;
    line-height: 1.2;
    color: var(--green);
  }
  .divider-vertical {
    width: 1px; height: 170px;
    background: linear-gradient(var(--card), #3a3a3a, var(--card));
    margin-right: 18px;
  }
  .contact { font-size: 12.5px; line-height: 1.55; }
  .person-name {
    font-family: "Cinzel", Georgia, serif;
    font-weight: 600;
    font-size: 19px;
    color: var(--green);
    letter-spacing: .5px;
    line-height: 1.2;
  }
  .person-title { font-size: 12px; margin-bottom: 4px; }
  .contact-row { display: flex; align-items: flex-start; gap: 7px; }
  .contact-row svg { flex: none; margin-top: 4px; fill: var(--green); }
  .contact-gap { height: 10px; }

  /* Location 2 – Plano */
  .card--plano {
    display: flex; flex-direction: column; align-items: center;
    justify-content: center;
  }
  .business-name {
    font-family: "Cinzel", Georgia, serif;
    color: var(--silver);
    text-align: center;
    font-weight: 600;
  }
  .business-name .main { display: block; font-size: 30px; letter-spacing: 1px; line-height: 1.1; }
  .business-name .sub { display: block; font-size: 11.5px; letter-spacing: .8px; }
  .location-line {
    display: flex; align-items: center; gap: 12px;
    margin-top: 8px;
    font-size: 11px;
  }
  .location-line .rule { width: 42px; height: 1px; background: var(--green-dark); }
  .phone-line {
    display: flex; gap: 18px; margin-top: 4px; font-size: 11px;
  }
  .phone-line span { display: flex; align-items: center; gap: 5px; }
  .phone-line svg { fill: var(--green); }
</style>
</head>
<body>

  <section class="card card--frisco" aria-label="Frisco location card">
    <div class="brand-name">
      <span class="brand-dot"></span>
      <span class="brand-text">Willow<br>Brook</span>
    </div>
    <div class="divider-vertical"></div>
    <div class="contact">
      <div class="person-name">LORIN DASKE</div>
      <div class="person-title">DC, MAOM, LAc (CA), CNS</div>
      <div class="contact-row">
        <svg width="11" height="9" viewBox="0 0 11 9"><path d="M0 0h11v9H0zM1 1.2v.6l4.5 3 4.5-3v-.6z"/></svg>
        <span>drlorindaske@mailnest.example</span>
      </div>
      <div class="contact-row">
        <svg width="10" height="10" viewBox="0 0 10 10"><circle cx="5" cy="5" r="5"/></svg>
        <span>www.drlorindaske.example</span>
      </div>
      <div class="contact-gap"></div>
      <div class="contact-row">
        <svg width="9" height="12" viewBox="0 0 9 12"><path d="M4.5 0A4.5 4.5 0 0 0 0 4.5C0 8 4.5 12 4.5 12S9 8 9 4.5A4.5 4.5 0 0 0 4.5 0zm0 6.3a1.8 1.8 0 1 1 0-3.6 1.8 1.8 0 0 1 0 3.6z"/></svg>
        <span>4817 Marlowe Blvd,<br>Suite B-100, Frisco, TX 75034</span>
      </div>
      <div class="contact-row">
        <svg width="10" height="10" viewBox="0 0 10 10"><path d="M2 0l2 2.4-1 1.3a6 6 0 0 0 3.3 3.3l1.3-1L10 8l-1.2 1.6C4.5 10 0 5.5.4 1.2z"/></svg>
        <span>(469) 555-0182</span>
      </div>
      <div class="contact-row">
        <svg width="10" height="10" viewBox="0 0 10 10"><path d="M2 0h5v3H2zM0 3.5h10V9H0zM2 6.5h6V10H2z"/></svg>
        <span>(972) 555-0137</span>
      </div>
    </div>
  </section>

  <section class="card card--plano" aria-label="Plano location card">
    <div class="business-name">
      <span class="main">WILLOW BROOK</span>
      <span class="sub">CHIROPRACTIC &amp; ACUPUNCTURE</span>
    </div>
    <div class="location-line">
      <span class="rule"></span>
      <span>1936 Belvane Road, Suite 100, Plano, TX 75075</span>
      <span class="rule"></span>
    </div>
    <div class="phone-line">
      <span><svg width="10" height="10" viewBox="0 0 10 10"><path d="M2 0l2 2.4-1 1.3a6 6 0 0 0 3.3 3.3l1.3-1L10 8l-1.2 1.6C4.5 10 0 5.5.4 1.2z"/></svg>(469) 555-0182</span>
      <span><svg width="10" height="10" viewBox="0 0 10 10"><path d="M2 0h5v3H2zM0 3.5h10V9H0zM2 6.5h6V10H2z"/></svg>(972) 555-0137</span>
    </div>
  </section>

</body>
</html>
```